convert my resume to an eye catching graphic resume

You must provide a sample desgin for my current Resume ... I'm including it in here....

I will pay 20 dollars - I would need the PSD file of this when you are done if you get picked for the job... I'm a Marketing Professional and this is all about making my Resume stand out in a good way... I don't like showing PHOTOS in a RESUME... so you need to make this look nice and sharp.

```html
<!DOCTYPE html>
<html lang="en">
<head>
<meta charset="utf-8">
<title>Tariq Selim Hadad – Resume</title>
<link rel="stylesheet" href="https://fonts.googleapis.com/css2?family=Dosis:wght@600;700;800&family=Barlow+Semi+Condensed:ital,wght@0,400;0,500;0,600;0,700;1,300;1,400&display=swap">
<style>
  :root{
    --blue:#1f9be0;
    --orange:#e8501e;
    --ink:#161616;
    --paper:#ffffff;
    --pie-green:#1f8a5b;
    --pie-dark:#1b2420;
    --pie-cyan:#1aa3d4;
  }
  *{margin:0;padding:0;box-sizing:border-box}
  html,body{width:848px;height:1200px;overflow:hidden;background:var(--paper)}
  body{font-family:"Barlow Semi Condensed",sans-serif;color:var(--ink);font-size:16.5px;line-height:20.7px}
  .resume{position:relative;width:848px;height:1200px}
  .name{position:absolute;left:16px;top:6px;font-family:"Dosis",sans-serif;font-weight:800;font-size:86px;line-height:80px;color:var(--blue);letter-spacing:1px;white-space:nowrap;text-transform:uppercase}
  .contact{position:absolute;left:22px;top:80px;color:var(--orange);font-size:16px;white-space:nowrap}
  .section-title{font-family:"Dosis",sans-serif;font-weight:700;font-size:35px;line-height:40px;color:var(--blue);position:absolute}
  .role{color:var(--orange);font-weight:600}
  .org{font-weight:600}
  .place{font-style:italic}
  .dates{font-style:italic;font-weight:300}
  .block{position:absolute}
  .job{margin-bottom:20.7px}
  .lang-row{display:flex;align-items:center;height:20.7px}
  .lang-name{width:200px;font-weight:600;font-size:17px}
  .lang-bar{margin-left:Auto;position:absolute;left:170px;height:13px;background:var(--orange);color:#fff;font-size:8px;line-height:13px;text-align:right;padding-right:4px}
  .tags{display:flex;flex-direction:column;gap:8px}
  .tag-row{display:flex;gap:7px;align-items:center}
  .tag{background:var(--orange);color:#fff;font-weight:500;font-size:17px;height:29px;line-height:29px;padding:0 11px;white-space:nowrap}
  .more{color:var(--orange);font-weight:600;font-size:17px}
  .edu{position:absolute;top:886px;font-size:16.5px}
  .edu .school{color:var(--orange);font-weight:600}
  .edu .years{color:var(--orange);font-weight:600;font-style:italic}
  .legend{position:absolute;left:186px;top:1047px;list-style:none;font-weight:600;font-size:17px}
  .legend li{position:relative;padding-left:27px;line-height:20.7px}
  .legend li::before{content:"";position:absolute;left:0;top:4px;width:13px;height:13px;background:var(--c)}
  .certs{position:absolute;right:21px;top:1044px;text-align:right;font-weight:600;font-size:17px;list-style:none}
  .footer{position:absolute;top:1172px;font-size:16.5px}
</style>
</head>
<body>
<main class="resume">
  <h1 class="name">Tariq Selim Hadad</h1>
  <p class="contact">+971500123456 – me@tshadad.net – http://tshadad.net – Villa # 42, St # 7c, Al Safa, Dubai, United Arab Emirates</p>

  <h2 class="section-title" style="left:19px;top:121px">Experience</h2>
  <section class="block" style="left:19px;top:178px;width:450px">
    <p class="job"><span class="role">Social Media And SEO Consultant</span> <span class="org">StoneKeep Ltd</span>, <span class="place">UK</span><br><span class="dates">Jan 2014 - Present</span> Providing SMM, SEM and SEO Consultation to Help Them Play Well on All Platforms</p>
    <p class="job"><span class="role">Social Media And Web Manager</span> <span class="org">WideReach Ltd</span>, <span class="place">UK</span><br><span class="dates">Sept 2013 - Jan 2014</span> Creating And Maintaining Social Media Campaigns and Engaging Users for 4 Online Stores</p>
    <p class="job"><span class="role">Inventory Administrator</span> <span class="org">WideReach Ltd</span>, <span class="place">UK</span><br><span class="dates">Feb 2013 - Sept 2013</span> Creating &amp; Maintaining Inventory Records and Listing Items on ShopBay/Marketa Stores</p>
    <p class="job"><span class="role">Store Manager</span> <span class="org">Noor Pharmacy</span>, <span class="place">Pakistan</span><br><span class="dates">Mar 2010 - Feb 2013</span> Supervising Salesmen, Increasing Revenue, Ledger Maintainance &amp; Maximizing Profitability</p>
    <p class="job"><span class="role">Individual Freelancer</span> <span class="org">GigHarbor.com</span>, <span class="place">Worldwide</span><br><span class="dates">July 2009 - Present</span> Providing Individual Web Development, SEO, Social Media Management &amp; Data Processing Services</p>
  </section>

  <h2 class="section-title" style="left:19px;top:603px">Failed Startups</h2>
  <section class="block" style="left:19px;top:660px;width:420px">
    <p><span class="role">Wavecast</span> Very First Radio Station for the youth of Pakistan</p>
    <p><span class="role">CampusCoders</span> Custom Web Design &amp; Development Firm</p>
    <p><span class="role">NewsNest</span> Online Platform to Earn Money by Sharing Interesting News and Information</p>
    <p><span class="role">HowToHub</span> Online How-To Magazine Custom Web Design &amp; Development Firm</p>
    <p><span class="role">Roamly</span> Tour <em>de</em> World</p>
  </section>

  <h2 class="section-title" style="left:19px;top:832px">Education</h2>
  <div class="edu" style="left:19px;width:270px"><p class="school">Higher Secondary School</p><p class="years">2008 – 2010</p><p>Northern Board of Intermediate and Secondary Education, Islamabad</p></div>
  <div class="edu" style="left:297px;width:290px"><p class="school">Diploma of Information Technology</p><p class="years">2010 – 2012</p><p>Capital Institute of Computing Sciences, Rawalpindi</p></div>
  <div class="edu" style="left:595px;width:240px"><p class="school">BS Software Engineering</p><p class="years">2011 – 2015</p><p>Margalla Technical University Islamabad – MTU</p></div>

  <h2 class="section-title" style="left:19px;top:987px">Hobbies</h2>
  <svg class="hobby-chart" style="position:absolute;left:22px;top:1044px" width="140" height="140" viewBox="0 0 140 140" role="img" aria-label="Pie chart of hobbies">
    <path d="M70 70 L70 2 A68 68 0 0 1 134.7 49 Z" fill="var(--pie-green)"/>
    <path d="M70 70 L134.7 49 A68 68 0 0 1 110 125 Z" fill="var(--orange)"/>
    <path d="M70 70 L110 125 A68 68 0 0 1 30 125 Z" fill="var(--pie-cyan)"/>
    <path d="M70 70 L30 125 A68 68 0 0 1 70 2 Z" fill="var(--pie-dark)"/>
    <g fill="#fff" font-family="Barlow Semi Condensed, sans-serif" font-size="9" font-weight="700" text-anchor="middle">
      <text x="99" y="36">20%</text><text x="120" y="92">20%</text><text x="70" y="124">20%</text><text x="16" y="62">40%</text>
    </g>
  </svg>
  <ul class="legend">
    <li style="--c:var(--orange)">Random Photography</li>
    <li style="--c:var(--pie-green)">Swimming &amp; Exercise</li>
    <li style="--c:var(--pie-dark)">Generating &amp; Executing<br>New Ideas</li>
    <li style="--c:var(--pie-cyan)">Reading Success Stories</li>
  </ul>

  <h2 class="section-title" style="left:486px;top:987px">Certifications</h2>
  <ul class="certs">
    <li>SEO Level 2 Certified via GigHarbor</li>
    <li>HTML Level 1 Certified via GigHarbor</li>
    <li>PressKit Level 1 Certified via GigHarbor</li>
    <li>Blogging Level 1 Certified via GigHarbor</li>
    <li>English Level 2 Certified via GigHarbor</li>
  </ul>

  <h2 class="section-title" style="left:477px;top:121px">Skills &amp; Specialities</h2>
  <section class="block" style="left:477px;top:178px;width:350px">
    <p><span class="role">Web Development</span> HTML, CSS, PHP, PressKit, SiteForge, CartCore, NodeCMS</p>
    <p><span class="role">Online Marketing</span> SEO, SEM, AdBoost, Affiliate &amp; Email Marketing, Retargeting.</p>
    <p><span class="role">Social Media</span> Branding, Promotions, Ads Campaigns.</p>
    <p><span class="role">Good Technical Understanding</span> Responsive Designs, Mobile Apps, Coding Languages.</p>
    <p><span class="role">Positive Thinking</span> Always..</p>
  </section>

  <h2 class="section-title" style="left:477px;top:390px">Languages</h2>
  <section class="block" style="left:477px;top:445px;width:330px">
    <div class="lang-row"><span class="lang-name">Urdu</span><span class="lang-bar" style="width:104px">100%</span></div>
    <div class="lang-row"><span class="lang-name">Hindi</span><span class="lang-bar" style="width:94px">90%</span></div>
    <div class="lang-row"><span class="lang-name">Punjabi</span><span class="lang-bar" style="width:104px">100%</span></div>
    <div class="lang-row"><span class="lang-name">English</span><span class="lang-bar" style="width:84px">80%</span></div>
    <div class="lang-row"><span class="lang-name">Arabic</span><span class="lang-bar" style="width:21px">20%</span></div>
  </section>

  <h2 class="section-title" style="left:477px;top:573px">Fimiliar with</h2>
  <section class="block tags" style="left:487px;top:631px">
    <div class="tag-row"><span class="tag">SlideDeck</span><span class="tag">GridSheet</span><span class="tag">DocWriter</span></div>
    <div class="tag-row"><span class="tag">AdBoost</span><span class="tag">AdYield</span><span class="tag">Analytics</span></div>
    <div class="tag-row"><span class="tag">ReTarget</span><span class="tag">ReviewHub</span><span class="tag">PostPigeon</span></div>
    <div class="tag-row"><span class="tag">Cloud Suite</span><span class="tag">Recomo</span><span class="tag">HostPanel</span></div>
    <div class="tag-row"><span class="tag">ListPro</span><span class="tag">ShopBay Store</span><span class="tag">MotionKit</span></div>
    <div class="tag-row"><span class="tag">PixelShop</span><span class="tag">WebLoom</span><span class="more">&amp; More..</span></div>
  </section>

  <p class="footer" style="left:17px">Online Resume: <em>http://cv.tshadad.net</em></p>
  <p class="footer" style="right:21px">Reference will be furnished on demand</p>
</main>
</body>
</html>
```